RQS Brochure

I would like to update our brochure and add additional services as well as change our logo, We are a full service PEO and a full service Payroll company
Target Market(s)
Business to Business
Industry/Entity Type
Payroll and Benefits
Font styles to use
Sans Serif

```html
<!DOCTYPE html>
<html lang="en">
<head>
<meta charset="utf-8">
<title>RQS Brochure</title>
<link href="https://fonts.googleapis.com/css2?family=Libre+Baskerville:wght@400;700&family=Open+Sans:wght@400;600;700&display=swap" rel="stylesheet">
<style>
:root{
  --stage:#8c8c8c;
  --paper:#ffffff;
  --maroon:#5b1a12;
  --maroon-dark:#3f100a;
  --amber:#d98a2b;
  --amber-light:#f0b35a;
  --cream:#f7ecdc;
  --ink:#3a2a24;
  --muted:#7a6a62;
  --rule:#e2cfb6;
}
*{box-sizing:border-box;margin:0;padding:0}
html,body{width:867px;height:1200px;overflow:hidden}
body{background:var(--stage);font-family:"Open Sans",Arial,sans-serif;color:var(--ink);position:relative}
.page{position:absolute;width:280px;height:388px;background:var(--paper);overflow:hidden;box-shadow:0 1px 3px rgba(0,0,0,.35)}
.p1{left:8px;top:8px}.p2{left:294px;top:8px}.p3{left:580px;top:8px}
.p4{left:8px;top:402px}.p5{left:294px;top:402px}.p6{left:580px;top:402px}
.p7{left:8px;top:796px}
.abs{position:absolute}
.serif{font-family:"Libre Baskerville",Georgia,serif}
.inner{position:absolute;left:14px;right:14px;top:12px;bottom:14px;display:flex;flex-direction:column;justify-content:space-between}
.body-text{font-size:5.2px;line-height:1.55;color:var(--ink)}
.body-text p+p{margin-top:4px}
.h-small{font-size:7.5px;font-weight:700;color:var(--maroon);text-transform:uppercase;letter-spacing:.3px}
.h-sub{font-size:6px;font-weight:700;color:var(--amber);margin-bottom:3px}
.circle{border-radius:50%}
.photo{background:linear-gradient(135deg,#c88a4a,#7a4322);flex:none}
.ring{border:2px solid var(--amber-light)}
.row{display:flex;gap:10px;align-items:flex-start}
.col{flex:1;min-width:0}
.cream-box{background:var(--cream);border-top:2px solid var(--amber);padding:7px 8px}

/* cover */
.cover-hero{left:0;top:0;width:280px;height:178px;background:radial-gradient(ellipse at 60% 30%,#f6c56a,#c8651e 55%,#4a1a0c);border-bottom-left-radius:60% 28px;border-bottom-right-radius:60% 28px}
.cover-title{left:14px;top:96px;width:200px;color:#fff;font-size:14px;line-height:1.3}
.cover-trio{left:20px;top:190px;width:240px;display:flex;justify-content:space-between}
.trio-item{width:66px;text-align:center}
.trio-img{width:52px;height:52px;margin:0 auto 4px}
.trio-cap{font-size:5px;color:var(--muted);line-height:1.3}
.brand{display:flex;align-items:center;gap:6px}
.brand-dot{width:22px;height:22px;border-radius:50%;border:2px solid var(--amber)}
.brand-name{font-size:20px;font-weight:700;color:var(--maroon);letter-spacing:1px}
.cover-brand{left:104px;top:284px}
.url-band{left:0;bottom:0;width:280px;height:30px;background:var(--maroon);color:#fff;font-size:7px;display:flex;align-items:center;padding-left:14px;letter-spacing:.4px}

/* lists */
.tick-list{list-style:none}
.tick-list li{display:flex;gap:4px;align-items:flex-start;margin-bottom:4px}
.tick-list svg{flex:none;width:6px;height:6px;margin-top:1px}
.bullets{list-style:none;font-size:5.2px;line-height:1.6}
.bullets li::before{content:"•";color:var(--amber);margin-right:3px}
.icon-row{display:flex;gap:4px;align-items:center;margin-bottom:2px;font-weight:700;color:var(--maroon)}
.mini-icon{width:9px;height:9px;border-radius:50%;background:var(--amber);flex:none}
.section{margin-bottom:9px}

/* table */
.compare{border-collapse:collapse;width:100%;font-size:4.9px;line-height:1.45}
.compare th{background:var(--maroon);color:#fff;text-align:left;padding:5px 4px;font-weight:600}
.compare td{padding:6px 4px;border-bottom:1px solid var(--rule);vertical-align:top}
.compare td:first-child{background:var(--maroon-dark);color:#fff;font-weight:600;width:62px}
.compare tr:nth-child(even) td:not(:first-child){background:var(--cream)}

/* back cover */
.back-photo{left:0;top:0;width:280px;height:388px;background:linear-gradient(160deg,#8a5a30 0%,#c27a3a 35%,#e09a45 60%,#d4852e 100%)}
.back-title{left:30px;top:140px;width:220px;text-align:center;color:#fff;font-size:14px;line-height:1.3}
.contact-row{left:40px;top:222px;width:200px;display:flex;justify-content:space-between}
.contact-item{width:60px;text-align:center;color:#fff;font-size:4.6px;line-height:1.3}
.contact-icon{width:28px;height:28px;border-radius:50%;background:var(--maroon);margin:0 auto 4px;display:flex;align-items:center;justify-content:center}
.contact-icon svg{width:13px;height:13px}
.back-brand{left:104px;top:290px}
.back-brand .brand-name{color:#fff}
.back-brand .brand-dot{border-color:#fff}
</style>
</head>
<body>

<section class="page p1">
  <div class="abs cover-hero" role="img" aria-label="Hands joining puzzle pieces against a sunset sky"></div>
  <h1 class="abs cover-title serif">Your Certified PEO/Payroll &amp; Human Resource Professionals</h1>
  <div class="abs cover-trio">
    <div class="trio-item"><div class="trio-img circle photo ring" role="img" aria-label="Stack of coins"></div><p class="trio-cap">Payroll Services</p></div>
    <div class="trio-item"><div class="trio-img circle photo ring" role="img" aria-label="Business handshake"></div><p class="trio-cap">PEO Partnership</p></div>
    <div class="trio-item"><div class="trio-img circle photo ring" role="img" aria-label="Team meeting"></div><p class="trio-cap">HR Support</p></div>
  </div>
  <div class="abs brand cover-brand"><span class="brand-dot"></span><span class="brand-name">RQS</span></div>
  <div class="abs url-band">www.rqspayroll.com</div>
</section>

<section class="page p2">
  <div class="inner">
    <div class="row">
      <div class="col body-text">
        <h2 class="h-small" style="margin-bottom:5px">About RQS Employee Services</h2>
        <p>RQS is a full service PEO and payroll company helping businesses manage people, pay and compliance with one trusted partner.</p>
      </div>
      <div class="photo" style="width:100px;height:52px" role="img" aria-label="Wooden stacks of coins"></div>
    </div>
    <div class="row">
      <div class="col body-text">
        <p>We handle payroll processing, tax filing, benefits and HR so owners can focus on growth. Our team brings years of experience to every client relationship.</p>
        <p>Every client receives a dedicated representative and clear reporting, backed by secure online access around the clock.</p>
      </div>
      <div class="photo circle ring" style="width:52px;height:52px" role="img" aria-label="Smiling businesswoman"></div>
    </div>
    <div>
      <h3 class="h-sub">Our Business</h3>
      <ul class="tick-list body-text">
        <li><svg viewBox="0 0 10 10"><path d="M1 5l3 3 5-7" fill="none" stroke="#d98a2b" stroke-width="2"/></svg>Accurate payroll processing with full tax filing, deposits and year end forms for every employee.</li>
        <li><svg viewBox="0 0 10 10"><path d="M1 5l3 3 5-7" fill="none" stroke="#d98a2b" stroke-width="2"/></svg>Benefits administration including health, dental, vision, life and retirement plans.</li>
        <li><svg viewBox="0 0 10 10"><path d="M1 5l3 3 5-7" fill="none" stroke="#d98a2b" stroke-width="2"/></svg>Workers compensation coverage with claims management and safety support.</li>
        <li><svg viewBox="0 0 10 10"><path d="M1 5l3 3 5-7" fill="none" stroke="#d98a2b" stroke-width="2"/></svg>Human resource guidance, employee handbooks and policy development.</li>
        <li><svg viewBox="0 0 10 10"><path d="M1 5l3 3 5-7" fill="none" stroke="#d98a2b" stroke-width="2"/></svg>Regulatory compliance monitoring at federal, state and local levels.</li>
        <li><svg viewBox="0 0 10 10"><path d="M1 5l3 3 5-7" fill="none" stroke="#d98a2b" stroke-width="2"/></svg>Time and attendance tools with online employee self-service access.</li>
      </ul>
    </div>
    <p class="body-text">Our clients range from local shops to multi state firms. Each one gains the same careful service, fast answers and a partner who understands the daily pressure of running a business.</p>
    <div class="cream-box body-text">Partnering with RQS means less paperwork, lower risk and more time for the work that matters most to your business and your people.</div>
  </div>
</section>

<section class="page p3">
  <div class="inner">
    <div class="row" style="align-items:center">
      <h2 class="col h-small">Certified PEO</h2>
      <div class="photo" style="width:90px;height:46px" role="img" aria-label="Professionals at a desk"></div>
    </div>
    <div class="row">
      <div class="col body-text">
        <h3 class="h-sub">What Does a PEO Do?</h3>
        <p>A PEO shares employer duties with your company, handling payroll, benefits and compliance while you keep control of daily operations and staff decisions.</p>
        <p>Pooled buying power gives small firms access to quality benefits at a lower cost than they could find alone.</p>
        <div class="cream-box" style="margin-top:6px">Certified status means our financial and tax practices are independently reviewed each year.</div>
      </div>
      <div class="col body-text">
        <p>Our certification offers added protection for clients and confirms that payroll taxes are paid correctly and on time.</p>
        <h3 class="h-sub" style="margin-top:6px">Benefits to You</h3>
        <ul class="bullets">
          <li>Reduced employer liability</li>
          <li>Better benefit options</li>
          <li>Expert HR assistance</li>
          <li>Simplified compliance</li>
          <li>Saved time and cost</li>
          <li>One point of contact</li>
        </ul>
      </div>
    </div>
    <div class="row" style="align-items:center">
      <div class="col body-text">
        <h3 class="h-sub">Growing With You</h3>
        <p>Whether you employ five people or five hundred, RQS scales with your needs and adapts as your company grows into new markets.</p>
        <p>New locations, seasonal staff and changing rules are handled by our team so nothing slips through.</p>
      </div>
      <div class="photo circle ring" style="width:62px;height:62px" role="img" aria-label="Business team"></div>
    </div>
    <p class="body-text">Contact our team to learn how a certified PEO relationship can strengthen your business and support your employees every single day.</p>
  </div>
</section>

<section class="page p4">
  <div class="inner" style="justify-content:flex-start;gap:12px">
    <div class="row" style="align-items:center">
      <div class="photo circle" style="width:46px;height:46px" role="img" aria-label="Coins and paperwork"></div>
      <div class="col">
        <h2 class="h-small">PEO vs ASO</h2>
        <p class="h-sub" style="margin:2px 0 0">Key Differences &amp; Similarities</p>
      </div>
    </div>
    <table class="compare">
      <tr><th>Feature</th><th>PEO</th><th>ASO</th></tr>
      <tr><td>Employer of record</td><td>Co-employment shared between client and PEO</td><td>Client remains the sole employer of record</td></tr>
      <tr><td>Payroll taxes</td><td>Filed and paid under the PEO tax ID</td><td>Filed and paid under the client tax ID</td></tr>
      <tr><td>Benefits</td><td>Access to large pooled group plans</td><td>Client sources and holds its own plans</td></tr>
      <tr><td>Workers comp</td><td>Covered by the PEO master policy</td><td>Client purchases its own policy</td></tr>
      <tr><td>HR support</td><td>Full HR guidance included in service</td><td>HR services chosen a la carte</td></tr>
      <tr><td>Compliance risk</td><td>Shared responsibility with the PEO</td><td>Retained fully by the client</td></tr>
      <tr><td>Pricing</td><td>Bundled fee per employee or payroll</td><td>Flat fee per service selected</td></tr>
      <tr><td>Best suited for</td><td>Small and fast growing firms</td><td>Larger established firms with HR staff</td></tr>
    </table>
  </div>
</section>

<section class="page p5">
  <div class="inner">
    <div class="row" style="align-items:center">
      <div class="photo circle" style="width:46px;height:46px" role="img" aria-label="Coins stacked on a desk"></div>
      <h2 class="col h-small">RQS Workforce Services</h2>
    </div>
    <div>
      <h3 class="h-sub">Services Include</h3>
      <div class="row body-text">
        <div class="col">
          <div class="icon-row"><span class="mini-icon"></span>Consulting</div>
          <p>Practical advice on staffing, policy and growth planning for owners.</p>
          <div class="icon-row" style="margin-top:5px"><span class="mini-icon"></span>Payroll</div>
          <p>Weekly or monthly payroll with direct deposit and tax filing.</p>
        </div>
        <div class="col">
          <div class="icon-row"><span class="mini-icon"></span>Online Self Service</div>
          <p>Employees view pay stubs, tax forms and benefits anytime.</p>
          <div class="icon-row" style="margin-top:5px"><span class="mini-icon"></span>Time Tracking</div>
          <p>Simple clock in tools linked directly to payroll.</p>
        </div>
      </div>
    </div>
    <div class="photo" style="height:80px" role="img" aria-label="Group of smiling office workers"></div>
    <div class="cream-box body-text">
      <p class="h-sub">Human Resources and Compliance</p>
      <p>From hiring to retirement we keep records current and help you meet changing labor rules with confidence. Our specialists review postings, forms and policies so your business stays protected.</p>
    </div>
  </div>
</section>

<section class="page p6">
  <div class="inner" style="flex-direction:row;gap:10px;justify-content:flex-start">
    <div class="col body-text" style="display:flex;flex-direction:column;justify-content:space-between">
      <div><p class="h-sub">Benefits Administration</p>
        <ul class="bullets"><li>Medical and dental</li><li>Vision and life</li><li>Retirement plans</li><li>Flexible spending</li><li>Enrollment support</li></ul></div>
      <div><p class="h-sub">Risk Management</p>
        <p>Safety programs and claims support that reduce workplace injuries and lower insurance cost over time.</p></div>
      <div><p class="h-sub">Coaching &amp; Training</p>
        <ul class="bullets"><li>Manager training</li><li>Onboarding sessions</li><li>Performance reviews</li><li>Conflict resolution</li></ul></div>
      <div><p class="h-sub">Recruiting Support</p>
        <p>Job postings, screening and background checks that help you hire the right people faster.</p></div>
      <div><p class="h-sub">Retirement Services</p>
        <p>Simple plan setup and payroll linked contributions for every eligible employee.</p></div>
    </div>
    <div class="col body-text" style="display:flex;flex-direction:column;justify-content:space-between">
      <div><p class="h-sub">Employee Onboarding</p>
        <p>Paperless new hire forms and quick setup for every employee on day one.</p></div>
      <div><p class="h-sub">Management Tools</p>
        <ul class="bullets"><li>Custom reports</li><li>Labor cost tracking</li><li>Secure records</li><li>Mobile approvals</li></ul></div>
      <div><p class="h-sub">Tax Credit Programs</p>
        <p>We identify hiring credits that can lower your annual tax bill.</p></div>
      <div><p class="h-sub">Unemployment Claims</p>
        <p>Timely responses that protect your rates and reserves.</p></div>
      <div><p class="h-sub">Employee Assistance</p>
        <p>Confidential support lines that help staff with personal and work concerns.</p></div>
    </div>
  </div>
</section>

<section class="page p7">
  <div class="abs back-photo" role="img" aria-label="Woman working on a laptop in warm light"></div>
  <h2 class="abs back-title serif">Contact Us Today for More Information</h2>
  <div class="abs contact-row">
    <div class="contact-item"><div class="contact-icon"><svg viewBox="0 0 24 24"><path d="M6 2l4 4-2 3c1 3 4 6 7 7l3-2 4 4-3 4C11 21 3 13 2 5z" fill="#fff"/></svg></div>(555) 014-2290</div>
    <div class="contact-item"><div class="contact-icon"><svg viewBox="0 0 24 24"><path d="M12 2a7 7 0 0 0-7 7c0 5 7 13 7 13s7-8 7-13a7 7 0 0 0-7-7zm0 10a3 3 0 1 1 0-6 3 3 0 0 1 0 6z" fill="#fff"/></svg></div>120 Harbor Way, Suite 4</div>
    <div class="contact-item"><div class="contact-icon"><svg viewBox="0 0 24 24"><path d="M2 5h20v14H2z" fill="#fff"/><path d="M2 5l10 8 10-8" fill="none" stroke="#5b1a12" stroke-width="2"/></svg></div>info@rqspayroll.com</div>
  </div>
  <div class="abs brand back-brand"><span class="brand-dot"></span><span class="brand-name">RQS</span></div>
  <div class="abs url-band">www.rqspayroll.com</div>
</section>

</body>
</html>
```